Ridgely Forge business card for handing simple contact information and generating service awareness

Utilizing the attached logo(s), generate a professional, but approachable, card conveying a sense of capability and integrity. Please only use one logo of the four attached; the different colors are all acceptable, but preference will be given to a design integrating a teal/turquoise logo,

I do not know where to put in the contact information or details?

Target Market(s)

Agriculture, Farming, Timber, Forestry, Construction, Crane Service

Industry/Entity Type

Contact Information for Business Card

Name, Phone Number, email address

Colors

Designer to choose colors to be used in the design.

Requirements
Nice to have
• It would be great to have either a mountain or one of the attached cranes as a backdrop on the rear of the card. Simple watermarks and/or Debossing is also great

```html
<!DOCTYPE html>
<html lang="en">
<head>
<meta charset="utf-8">
<title>Ridgely Forge – Business Card</title>
<link href="https://fonts.googleapis.com/css2?family=Open+Sans:wght@400;700;800&display=swap" rel="stylesheet">
<style>
  :root {
    --backdrop: #2b2c2f;
    --card: #1c1d20;
    --accent: #00aee8;
    --ink-light: #f2f2f2;
    --ink-muted: #cfd3d6;
  }
  * { margin: 0; padding: 0; box-sizing: border-box; }
  html, body { width: 1200px; height: 780px; overflow: hidden; }
  body {
    background: var(--backdrop);
    font-family: "Open Sans", Arial, sans-serif;
    display: flex;
    align-items: center;
    justify-content: center;
    gap: 60px;
  }
  .card {
    width: 520px;
    height: 300px;
    background: var(--card);
    border-radius: 22px;
    position: relative;
    overflow: hidden;
  }
  .brand {
    display: flex;
    align-items: center;
    gap: 10px;
    color: var(--accent);
    font-weight: 800;
    text-transform: uppercase;
    letter-spacing: 0.02em;
    white-space: nowrap;
  }
  .brand-dot {
    border-radius: 50%;
    background: var(--accent);
    flex: none;
  }
  /* Front */
  .card-front .brand {
    position: absolute;
    left: 30px;
    top: 128px;
    font-size: 22px;
  }
  .card-front .brand-dot { width: 22px; height: 22px; }
  .divider {
    position: absolute;
    left: 250px;
    top: 46px;
    width: 1px;
    height: 208px;
    background: var(--accent);
  }
  .contact {
    position: absolute;
    left: 276px;
    top: 50px;
    color: var(--ink-light);
  }
  .contact-name {
    color: var(--accent);
    font-weight: 700;
    font-size: 24px;
    line-height: 1.1;
    text-transform: uppercase;
  }
  .contact-role {
    font-size: 15px;
    margin-bottom: 12px;
  }
  .contact-list { list-style: none; font-size: 15px; line-height: 1.45; }
  .contact-list li { display: flex; align-items: center; gap: 8px; }
  .contact-list svg { width: 13px; height: 13px; flex: none; }
  .contact-address { font-size: 15px; line-height: 1.35; margin-top: 8px; }
  /* Back */
  .card-back { display: flex; align-items: center; justify-content: center; }
  .card-back .brand { font-size: 36px; gap: 14px; }
  .card-back .brand-dot { width: 34px; height: 34px; }
</style>
</head>
<body>
  <section class="card card-front">
    <div class="brand"><span class="brand-dot"></span>Ridgely Forge</div>
    <div class="divider"></div>
    <div class="contact">
      <p class="contact-name">Owen Hartley</p>
      <p class="contact-role">Managing Director</p>
      <ul class="contact-list">
        <li>
          <svg viewBox="0 0 16 16" aria-hidden="true"><path fill="var(--accent)" d="M3.6 1.2l2.3 2.6-1.3 1.9c.9 2 2.4 3.6 4.5 4.6l1.9-1.3 2.7 2.3-1.4 2.3C7.8 14.5 1.6 8.4 1.4 2.6z"/></svg>
          123 456 789
        </li>
        <li>
          <svg viewBox="0 0 16 16" aria-hidden="true"><rect x="1" y="3" width="14" height="10" rx="1.5" fill="var(--accent)"/><path d="M1.5 4l6.5 5 6.5-5" stroke="var(--card)" stroke-width="1.4" fill="none"/></svg>
          info@yourgmail.com
        </li>
        <li>
          <svg viewBox="0 0 16 16" aria-hidden="true"><circle cx="8" cy="8" r="6.5" fill="none" stroke="var(--accent)" stroke-width="1.6"/><path d="M1.5 8h13M8 1.5c-3 3.5-3 9.5 0 13M8 1.5c3 3.5 3 9.5 0 13" stroke="var(--accent)" stroke-width="1.2" fill="none"/></svg>
          www.yourwebsite.com
        </li>
      </ul>
      <p class="contact-address">Your address, City<br>State, Zip 1234</p>
    </div>
  </section>

  <section class="card card-back">
    <div class="brand"><span class="brand-dot"></span>Ridgely Forge</div>
  </section>
</body>
</html>
```